PebbleLoop screens tidy up

We would like advice on how to better present the following home page and overview pages.

The existing website is functional, but the pages don't appear professionals and pleasing to the eye. We would specifically like feedback on alignment and padding of icons and text to make the screen more appealing and polished.

We are following the quartz design system.

Number of Pages Required

1 page

Font styles to use
Sans Serif
Other font styles liked:
• IBM Plex, Poppins

```html
<!DOCTYPE html>
<html lang="en">
<head>
<meta charset="utf-8">
<title>PebbleLoop – Home</title>
<link rel="stylesheet" href="https://fonts.googleapis.com/css2?family=IBM+Plex+Sans:wght@300;400;500;600&display=swap">
<style>
:root{
  --shell:#3b3937;
  --shell-line:#2a2827;
  --page:#ebebeb;
  --surface:#ffffff;
  --text:#161616;
  --text-soft:#525252;
  --line:#d0d0d0;
  --accent:#0f62fe;
  --sand:#ecd3b2;
  --sand-deep:#e2bf92;
  --hex-grey:#d4d4d4;
  --hex-dark:#5e5e5e;
  --nav-active:#eeeeee;
}
*{box-sizing:border-box;margin:0;padding:0}
html,body{width:1200px;height:1000px;overflow:hidden;background:#fff;font-family:"IBM Plex Sans",Arial,sans-serif;color:var(--text)}
.app{position:relative;width:1200px;height:840px}
.topbar{position:absolute;left:0;top:0;width:1200px;height:31px;background:var(--shell);border-bottom:1px solid var(--shell-line)}
.brand{position:absolute;left:11px;top:7px;display:flex;align-items:center;gap:6px;color:#fff;font-size:12px;font-weight:600}
.brand-dot{width:15px;height:15px;border-radius:50%;background:#e8a33b}
.avatar{position:absolute;right:9px;top:6px}
.sidenav{position:absolute;left:0;top:31px;width:194px;height:809px;background:var(--surface);border-left:1px solid #888;border-right:1px solid var(--line)}
.nav-item{position:absolute;left:0;width:193px;height:25px;display:flex;align-items:center;padding-left:11px;gap:6px;font-size:10px;color:#333}
.nav-item.is-active{background:var(--nav-active);border-left:3px solid var(--accent);padding-left:8px}
.nav-item svg{flex:none}
.nav-heading{position:absolute;left:11px;top:94px;font-size:10px;font-weight:600;width:175px}
.nav-heading span{position:absolute;right:0;top:-3px;font-size:14px;font-weight:400}
.campaign-row{position:absolute;left:0;width:193px;height:26px;display:flex;align-items:center;padding-left:7px;gap:8px;font-size:10.5px;color:#222;border-bottom:1px solid var(--line)}
.campaign-row.is-open{background:#ececec}
.campaign-row .chip{width:18px;height:18px;border-radius:50%;background:#d6d6d6}
.campaign-row .caret{position:absolute;right:9px;font-size:9px;color:#777}
.sub-item{position:absolute;left:33px;font-size:10px;color:#333}
.nav-divider{position:absolute;left:0;top:277px;width:193px;border-top:1px solid var(--line)}
.collapse{position:absolute;left:170px;top:790px;font-size:13px;color:#333}
.page-head{position:absolute;left:194px;top:31px;width:1006px;height:61px;background:var(--shell)}
.page-head h1{position:absolute;left:19px;top:28px;font-size:24px;font-weight:300;color:#fff}
.content{position:absolute;left:194px;top:92px;width:1006px;height:630px;background:var(--page)}
.label{position:absolute;font-size:10px;font-weight:600}
.card{position:absolute;background:var(--surface)}
.teamspace h2{position:absolute;left:13px;top:6px;font-size:19px;font-weight:400}
.teamspace p{position:absolute;left:13px;top:35px;font-size:9px;color:var(--text-soft)}
.decor{position:absolute}
.usage-title{position:absolute;left:10px;top:65px;font-size:10.5px}
.usage-bar{position:absolute;left:10px;top:81px;width:452px;border-top:1px solid #bdbdbd}
.usage-note{position:absolute;left:10px;top:87px;font-size:7.5px;color:var(--text-soft)}
.stat-caption{position:absolute;left:51px;top:7px;font-size:9px;color:var(--text-soft)}
.stat-num{position:absolute;font-size:24px;font-weight:500}
.btn-primary{position:absolute;left:890px;top:297px;width:93px;height:19px;background:var(--accent);color:#fff;font-size:8px;display:flex;align-items:center;justify-content:center;gap:8px}
.campaign-banner{position:absolute;left:25px;top:324px;width:958px;height:251px;background:linear-gradient(90deg,var(--sand) 0%,#f6e6d1 50%,var(--sand) 100%)}
.campaign-card{position:absolute;top:338px;width:192px;height:210px;background:var(--surface);box-shadow:0 1px 2px rgba(0,0,0,.15);text-align:center}
.campaign-card h3{margin-top:4px;font-size:15px;font-weight:400}
.campaign-card .desc{margin-top:3px;font-size:7.5px;color:var(--text-soft);white-space:nowrap;overflow:hidden;padding:0 8px}
.campaign-art{display:block;margin:12px auto 0;width:82px;height:82px;border-radius:50%;background:radial-gradient(circle,#eeeeee 0%,#d6d6d6 70%)}
.campaign-count{display:flex;justify-content:center;align-items:center;gap:6px;margin-top:15px;text-align:left}
.campaign-count b{font-size:26px;font-weight:300;color:var(--accent);line-height:1}
.campaign-count small{display:block;font-size:7px;color:var(--text-soft)}
.campaign-count strong{display:block;font-size:9.5px;font-weight:500}
.campaign-card .since{position:absolute;left:0;width:100%;top:196px;font-size:7.5px;color:var(--text-soft)}
.footer{position:absolute;left:194px;top:722px;width:1006px;height:118px;background:linear-gradient(180deg,#3a3836,#343231)}
</style>
</head>
<body>
<div class="app">
  <header class="topbar">
    <div class="brand"><span class="brand-dot"></span>PebbleLoop</div>
    <svg class="avatar" width="20" height="20" viewBox="0 0 20 20"><circle cx="10" cy="10" r="9" fill="#fff"/><circle cx="10" cy="8" r="3.2" fill="none" stroke="#333" stroke-width="1.4"/><path d="M4.5 16c1.5-3 9.5-3 11 0" fill="none" stroke="#333" stroke-width="1.4"/></svg>
  </header>

  <nav class="sidenav">
    <div class="nav-item is-active" style="top:0"><svg width="10" height="10" viewBox="0 0 10 10"><path d="M1 5 5 1.5 9 5v4H1z" fill="none" stroke="#333"/></svg>Home</div>
    <div class="nav-item" style="top:26px"><svg width="10" height="10" viewBox="0 0 10 10"><path d="M2 8h6M3 8V4a2 2 0 0 1 4 0v4" fill="none" stroke="#555"/></svg>All alerts</div>
    <div class="nav-item" style="top:51px"><svg width="10" height="10" viewBox="0 0 10 10"><circle cx="5" cy="5" r="3.5" fill="none" stroke="#555"/><circle cx="5" cy="5" r="1.2" fill="#555"/></svg>Manage</div>
    <div class="nav-heading">Campaigns<span>–</span></div>
    <div class="campaign-row is-open" style="top:117px"><span class="chip"></span>My custom campaign<span class="caret">︿</span></div>
    <div class="sub-item" style="top:151px">Overview</div>
    <div class="sub-item" style="top:177px">Files &amp; HoneyTokens</div>
    <div class="sub-item" style="top:203px">Resources</div>
    <div class="sub-item" style="top:228px">Alerts</div>
    <div class="sub-item" style="top:254px">Settings</div>
    <div class="nav-divider"></div>
    <div class="campaign-row" style="top:278px"><span class="chip"></span>Default campaign<span class="caret">﹀</span></div>
    <div class="collapse">«</div>
  </nav>

  <div class="page-head"><h1>Home</h1></div>

  <main class="content">
    <div class="label" style="left:23px;top:32px">Teamspace</div>
    <section class="card teamspace" style="left:23px;top:52px;width:961px;height:54px">
      <h2>Default</h2>
      <p>The default client is created as a part of your user account.</p>
    </section>

    <div class="label" style="left:23px;top:129px">Subscription overview</div>
    <section class="card" style="left:23px;top:148px;width:472px;height:128px">
      <svg class="decor" style="left:10px;top:8px" width="22" height="20" viewBox="0 0 22 20"><rect x="0" y="12" width="6" height="8" fill="#161616"/><rect x="8" y="6" width="6" height="14" fill="#161616"/><rect x="16" y="0" width="6" height="20" fill="#161616"/></svg>
      <div class="decor" role="img" aria-label="Decorative grey shapes" style="left:320px;top:0;width:152px;height:107px;background:linear-gradient(135deg,#fff 0%,var(--hex-grey) 60%,#bdbdbd 100%);opacity:.6"></div>
      <div class="usage-title">Starter pack usage</div>
      <div class="usage-bar"></div>
      <div class="usage-note">0 files active out of 10 allowed</div>
    </section>

    <div class="label" style="left:512px;top:129px">Files &amp; HoneyTokens</div>
    <section class="card" style="left:512px;top:148px;width:471px;height:128px">
      <svg class="decor" style="left:10px;top:6px" width="20" height="22" viewBox="0 0 20 22"><path d="M2 1h10l5 5v15H2z" fill="none" stroke="#222" stroke-width="1.3"/><path d="M5 9h9M5 12h9M5 15h9" stroke="#222"/></svg>
      <div class="stat-caption">Statistics</div>
      <div class="decor" role="img" aria-label="Decorative grey shape" style="left:110px;top:56px;width:68px;height:70px;border-radius:14px;background:var(--hex-grey);opacity:.55"></div>
      <svg class="decor" style="left:92px;top:84px" width="18" height="18" viewBox="0 0 18 18"><circle cx="9" cy="9" r="8" fill="none" stroke="#222" stroke-width="1.3"/><path d="M5 9l3 3 5-6" fill="none" stroke="#222" stroke-width="1.3"/></svg>
      <div class="stat-num" style="left:128px;top:76px">0</div>
      <div class="decor" role="img" aria-label="Decorative grey shape" style="left:338px;top:54px;width:108px;height:72px;border-radius:16px;background:var(--hex-grey);opacity:.55"></div>
      <svg class="decor" style="left:315px;top:84px" width="16" height="18" viewBox="0 0 16 18"><path d="M2 1h8l4 4v12H2z" fill="none" stroke="#222" stroke-width="1.2"/><path d="M4 8h8M4 11h8M4 14h8" stroke="#222"/></svg>
      <div class="stat-num" style="left:348px;top:76px">30</div>
    </section>

    <div class="label" style="left:23px;top:302px">Campaigns</div>
    <div class="btn-primary">New campaign <span>+</span></div>

    <div class="campaign-banner" role="img" aria-label="Decorative sand-coloured background pattern"></div>

    <article class="campaign-card" style="left:306px">
      <h3>My custom campaign</h3>
      <p class="desc">This is my custom campaign for finding i</p>
      <span class="campaign-art" role="img" aria-label="Illustration of files and gears"></span>
      <div class="campaign-count"><b>0</b><span><small>Active</small><strong>Files and HoneyTokens</strong></span></div>
      <div class="since">Active since: Jul 25 2023 13:12</div>
    </article>

    <article class="campaign-card" style="left:509px">
      <h3>Default campaign</h3>
      <p class="desc">Define your own mission, or combine differen...</p>
      <span class="campaign-art" role="img" aria-label="Illustration of files and gears"></span>
      <div class="campaign-count"><b>0</b><span><small>Active</small><strong>Files and HoneyTokens</strong></span></div>
      <div class="since">Active since: Jul 20 2023 12:17</div>
    </article>
  </main>

  <footer class="footer" role="img" aria-label="Dark decorative footer pattern"></footer>
</div>
</body>
</html>
```